Professional and modern website for Real Estate services company

Hi there! We're looking for a responsive, highly professional and modern (in line with Latest trends) coded website for a Real Estate services company named Portalia720º (find logo attached). I will try to Explain how I picture it in my head, but feel free to step out of the script and design it as you please. The structure for the website must be as Follows: - Menu: at the top of the screen, always visible (in any page and when to scrolling down). Logo at the left hand side (clicking redirects to home), then a Services, About us, Blog and Contact and on the right hand, Estimate and Log in (just placeholder, no log in required yet). - Home: (I like https://fr.domvera.example/): a landscape picture of Madrid's skyline. Very important That at a first glance (without scrolling) you can see a box to input data of your building to get an estimate (Post code, Number of homes, Number of garages, Number of stores, Swimming pool (yes / no) Concierge (yes / no)). Should there be a small space Also for a corporate presentation video (more or less like https://www.velbrastahogares.example/ but With the estimate Request box INSTEAD OF the App - however, do not take this one as example Given I just wanted to illustrate the structure). Still in the Home, bellow the first glance, I'd like to have a brief introduction of the following pages (Services, About us, Blog and Contact). This can be in a Either "square" form (like https://fr.domvera.example/) or in a "scroll" form (like https://k7pisos.example/). - Services: we offer 3 sets of services, each of them composed by three specific services, Namely: * Administration Treasury Accounting Savings * Consulting Legal Technical Regulatory * Mediation Repairs Meetings Delinquency For the sake of structuring, each of the nine services will Have to written description composed of 3 small paragraphs of About 15 words. I Tend to like to Accompany With each of the services related icons / vectors, but feel free to design them as you want. - About us: content not yet defined, but will be a series of bullets / sections in Which We talk about prep or differentiating points. We can include the corporate video presentation here again. - Blog: just a space Where you can see to the blog entries (in Home, probably just show 3/4). - Contact: a fancy contact form, with map, address, telephone, e-mail and opening hours. Just to give it a bit more content, maybe include a catch phrase like "We're looking forward to meeting you!" or something like that. - Estimate: this is the Most Important page in the website (in Addition to the upper part of the Home page). Basically replicate the estimate for the home box, but maybe with a bit more design or extended, Given this is a single page just for that. - Log in: opens a drop-down with user and password (just placeholder, no log in required yet). Regarding colors, we still do not Have a color scheme, so anything in line With the logo is OK. Many thanks in advance, Martin

All ages and genders

Real Estate

Coded - Design and coding required

5+ page

Sans Serif

Must have
• Blank colored background

```html
<!DOCTYPE html>
<html lang="en">
<head>
<meta charset="utf-8">
<title>Portalia720º — Real Estate Services</title>
<link rel="stylesheet" href="https://fonts.googleapis.com/css2?family=Lato:wght@400;700&family=Montserrat:wght@700&family=Questrial&display=swap">
<style>
:root{
  --orange:#d4730f;
  --orange-dark:#b85f08;
  --ink:#333333;
  --muted:#6f6f6f;
  --line:#cfcfcf;
  --panel:#f0f0f0;
  --white:#ffffff;
  --footer:#676767;
  --footer-field:#7a7a7a;
}
*{box-sizing:border-box;margin:0;padding:0}
html,body{width:1200px;height:3409px;overflow:hidden}
body{position:relative;background:var(--white);font-family:'Lato',sans-serif;color:var(--ink)}
.abs{position:absolute}

/* top bar */
.topbar{position:absolute;left:0;top:0;width:1200px;height:45px;background:var(--white);border-bottom:1px solid #e6e6e6;font-size:14px;color:var(--muted)}
.topbar .contact{position:absolute;top:13px;display:flex;align-items:center;gap:8px}
.social-sq{position:absolute;top:10px;width:25px;height:25px;border:1px solid #ddd;background:#fafafa}

/* nav */
.nav{position:absolute;left:0;top:45px;width:1200px;height:73px;background:var(--white)}
.brand{position:absolute;left:100px;top:22px;display:flex;align-items:center;gap:10px;font-family:'Lato',sans-serif;font-weight:700;font-size:26px;color:#555}
.brand .mark{width:16px;height:16px;background:var(--orange)}
.nav a{position:absolute;top:27px;font-size:14px;color:var(--ink);text-decoration:none}
.nav .util{display:flex;align-items:center;gap:7px}

/* hero */
.hero{position:absolute;left:0;top:118px;width:1200px;height:609px;background:linear-gradient(180deg,#c9a86f 0%,#8d8a86 25%,#6e6c6b 55%,#4a4845 100%)}
.hero h1{position:absolute;left:100px;top:344px;font-family:'Montserrat',sans-serif;font-size:41px;line-height:50px;color:var(--white);letter-spacing:.5px}
.hero .rule{position:absolute;left:100px;top:459px;width:570px;height:2px;background:rgba(255,255,255,.8)}
.dots{position:absolute;left:101px;top:497px;display:flex;gap:8px}
.dots span{width:11px;height:11px;border-radius:50%;background:rgba(255,255,255,.6)}
.dots span:first-child{background:var(--orange)}
.estimate-box{position:absolute;left:759px;top:177px;width:341px;height:471px;background:rgba(255,255,255,.35)}
.field{position:absolute;left:32px;width:282px;height:40px;background:rgba(255,255,255,.88);font-size:13px;color:#666;padding:0 14px;display:flex;align-items:center;justify-content:space-between}
.btn-submit{position:absolute;left:32px;top:391px;width:282px;height:43px;background:var(--orange);color:var(--white);font-family:'Montserrat',sans-serif;font-size:17px;display:flex;align-items:center;justify-content:center;letter-spacing:.5px}

/* section heads */
.sec-title{position:absolute;left:0;width:1200px;text-align:center;font-family:'Lato',sans-serif;font-size:38px;font-weight:400;color:#444}
.sec-rule{position:absolute;left:518px;width:240px;height:14px}

/* about */
.about{position:absolute;left:0;top:727px;width:1200px;height:575px;background:var(--white)}
.points{position:absolute;left:100px;top:165px;list-style:none}
.points li{display:flex;align-items:center;gap:18px;height:39.5px;font-size:17px;color:#333}
.monitor{position:absolute;left:657px;top:164px}

/* services */
.services{position:absolute;left:0;top:1302px;width:1200px;height:1182px;background:var(--panel)}
.cat{position:absolute;height:37px;border:2px solid var(--orange);color:var(--orange);font-family:'Lato',sans-serif;font-weight:700;font-size:20px;display:flex;align-items:center;justify-content:center;background:var(--panel)}
.cat-line{position:absolute;height:1px;background:var(--line)}
.card{position:absolute;width:316px;height:230px;background:var(--white);box-shadow:0 2px 4px rgba(0,0,0,.18)}
.card .photo{position:absolute;left:0;top:0;width:316px;height:168px}
.card .label{position:absolute;left:0;top:168px;width:316px;height:62px;display:flex;align-items:center;justify-content:center;font-family:'Questrial',sans-serif;font-size:25px;color:#222}
.card .badge{position:absolute;left:128px;top:124px}
.card.active{background:#3b2a1e}
.card.active .overlay{position:absolute;inset:0;background:linear-gradient(160deg,#4b3626,#221810);color:var(--white);text-align:center;padding-top:36px}
.overlay h3{font-family:'Questrial',sans-serif;font-weight:400;font-size:24px;margin-bottom:16px}
.overlay p{font-size:13px;font-weight:700;line-height:17px;padding:0 44px}
.overlay .plus{margin-top:22px}

/* blog */
.blog{position:absolute;left:0;top:2484px;width:1200px;height:589px;background:var(--white)}
.post{position:absolute;top:153px;width:316px;height:386px;background:var(--white);border:1px solid #e2e2e2;box-shadow:0 1px 3px rgba(0,0,0,.1)}
.post .photo{width:314px;height:195px}
.post h3{position:absolute;left:18px;top:218px;font-family:'Questrial',sans-serif;font-weight:400;font-size:20px;color:#222}
.post .meta{position:absolute;left:18px;top:248px;font-size:12px;color:#555;display:flex;gap:30px}
.post p{position:absolute;left:18px;top:270px;width:285px;font-size:13px;line-height:19px;color:#333}
.post .more{position:absolute;left:16px;top:322px;width:114px;height:40px;background:var(--orange);color:var(--white);font-size:15px;display:flex;align-items:center;justify-content:center;gap:10px}
.carousel-arrow{position:absolute;top:2810px}

/* footer */
.footer{position:absolute;left:0;top:3073px;width:1200px;height:336px;background:var(--footer);color:var(--white)}
.footer h4{position:absolute;top:42px;font-family:'Lato',sans-serif;font-weight:400;font-size:19px}
.quick-links{position:absolute;left:123px;top:94px;list-style:none;font-size:13px}
.quick-links li{height:34px}
.inq{position:absolute;left:332px;width:195px;height:29px;background:var(--footer-field);font-size:11px;color:#ddd;padding:8px 10px}
.inq-submit{position:absolute;left:336px;top:216px;width:80px;height:27px;background:var(--orange);font-size:13px;font-weight:700;display:flex;align-items:center;justify-content:center}
.detail{position:absolute;left:647px;display:flex;gap:10px;font-size:13px;line-height:17px}
.map{position:absolute;left:852px;top:3073px}
.bottom-bar{position:absolute;left:0;top:3364px;width:880px;height:45px;background:var(--orange);color:var(--white);font-size:13px}
.bottom-bar .copy{position:absolute;left:100px;top:14px}
.round{position:absolute;top:10px;width:26px;height:26px;border-radius:50%;background:var(--white)}
</style>
</head>
<body>

<!-- top bar -->
<div class="topbar">
  <div class="contact" style="left:100px">
    <svg width="16" height="12" viewBox="0 0 16 12"><rect width="16" height="12" fill="#d4730f"/><path d="M0 0l8 6 8-6" stroke="#fff" stroke-width="1.5" fill="none"/></svg>
    info@portalia720.example
  </div>
  <div class="contact" style="left:285px">
    <svg width="14" height="14" viewBox="0 0 14 14"><path d="M3 1l2.5 3-1.4 1.6a8 8 0 0 0 4.3 4.3L10 8.5 13 11l-1.5 2C6 13 1 8 1 2.5z" fill="#d4730f"/></svg>
    (012) 5550 1420
  </div>
  <div class="social-sq" style="left:996px"></div>
  <div class="social-sq" style="left:1035px"></div>
  <div class="social-sq" style="left:1074px"></div>
</div>

<!-- navigation -->
<nav class="nav">
  <div class="brand"><span class="mark"></span>Portalia720º</div>
  <a style="left:425px">About Us</a>
  <a style="left:532px">Services</a>
  <a style="left:641px">Blog</a>
  <a style="left:718px">Contact Us</a>
  <a class="util" style="left:916px"><span style="color:var(--orange);font-weight:700">$</span>Estimate</a>
  <a class="util" style="left:1036px">
    <svg width="14" height="13" viewBox="0 0 14 13"><path d="M0 5h7V2l5 4.5-5 4.5V8H0z" fill="#d4730f"/></svg>Log In
  </a>
</nav>

<!-- hero -->
<header class="hero" role="img" aria-label="Aerial view of Madrid's city skyline and a busy boulevard at dusk">
  <h1>NOW IT'S EASY TO FIND<br>YOUR FUTURE HOME</h1>
  <div class="rule"></div>
  <div class="dots"><span></span><span></span><span></span></div>
</header>
<form class="estimate-box">
  <div class="field" style="top:32px">Post Code</div>
  <div class="field" style="top:91px">Number of Homes<span>&#8661;</span></div>
  <div class="field" style="top:150px">Number of Garages<span>&#8661;</span></div>
  <div class="field" style="top:209px">Number of Stores<span>&#8661;</span></div>
  <div class="field" style="top:268px">Swimming Pool</div>
  <div class="field" style="top:328px">Concierge</div>
  <div class="btn-submit">SUBMIT</div>
</form>

<!-- about -->
<section class="about">
  <h2 class="sec-title" style="top:40px">About Us</h2>
  <svg class="sec-rule" style="top:97px" viewBox="0 0 240 14"><path d="M0 12H108L120 2 132 12H240" stroke="#b8b8b8" fill="none"/><path d="M113 12l7-6 7 6" stroke="#b8b8b8" fill="none"/></svg>
  <ul class="points">
    <li><svg width="18" height="16" viewBox="0 0 18 16"><rect x="1" y="3" width="12" height="12" fill="none" stroke="#d4730f" stroke-width="1.6"/><path d="M4 8l3 3 9-10" stroke="#d4730f" stroke-width="2" fill="none"/></svg>Lorem ipsum dolor sit amet, consectetuer adipiscing elit</li>
    <li><svg width="18" height="16" viewBox="0 0 18 16"><rect x="1" y="3" width="12" height="12" fill="none" stroke="#d4730f" stroke-width="1.6"/><path d="M4 8l3 3 9-10" stroke="#d4730f" stroke-width="2" fill="none"/></svg>Sed diam nonummy nibh euismod tincidunt ut laoree</li>
    <li><svg width="18" height="16" viewBox="0 0 18 16"><rect x="1" y="3" width="12" height="12" fill="none" stroke="#d4730f" stroke-width="1.6"/><path d="M4 8l3 3 9-10" stroke="#d4730f" stroke-width="2" fill="none"/></svg>&nbsp;Ut wisi enim ad minim veniam, quis nostrud exerci tation</li>
    <li><svg width="18" height="16" viewBox="0 0 18 16"><rect x="1" y="3" width="12" height="12" fill="none" stroke="#d4730f" stroke-width="1.6"/><path d="M4 8l3 3 9-10" stroke="#d4730f" stroke-width="2" fill="none"/></svg>Lorem ipsum dolor sit amet, consectetuer adipiscing elit</li>
    <li><svg width="18" height="16" viewBox="0 0 18 16"><rect x="1" y="3" width="12" height="12" fill="none" stroke="#d4730f" stroke-width="1.6"/><path d="M4 8l3 3 9-10" stroke="#d4730f" stroke-width="2" fill="none"/></svg>Sed diam nonummy nibh euismod tincidunt ut laoree</li>
    <li><svg width="18" height="16" viewBox="0 0 18 16"><rect x="1" y="3" width="12" height="12" fill="none" stroke="#d4730f" stroke-width="1.6"/><path d="M4 8l3 3 9-10" stroke="#d4730f" stroke-width="2" fill="none"/></svg>&nbsp;Ut wisi enim ad minim veniam, quis nostrud exerci tation</li>
    <li><svg width="18" height="16" viewBox="0 0 18 16"><rect x="1" y="3" width="12" height="12" fill="none" stroke="#d4730f" stroke-width="1.6"/><path d="M4 8l3 3 9-10" stroke="#d4730f" stroke-width="2" fill="none"/></svg>Lorem ipsum dolor sit amet, consectetuer adipiscing elit</li>
    <li><svg width="18" height="16" viewBox="0 0 18 16"><rect x="1" y="3" width="12" height="12" fill="none" stroke="#d4730f" stroke-width="1.6"/><path d="M4 8l3 3 9-10" stroke="#d4730f" stroke-width="2" fill="none"/></svg>Sed diam nonummy nibh euismod tincidunt ut laoree</li>
    <li><svg width="18" height="16" viewBox="0 0 18 16"><rect x="1" y="3" width="12" height="12" fill="none" stroke="#d4730f" stroke-width="1.6"/><path d="M4 8l3 3 9-10" stroke="#d4730f" stroke-width="2" fill="none"/></svg>&nbsp;Ut wisi enim ad minim veniam, quis nostrud exerci tation</li>
  </ul>
  <svg class="monitor" width="443" height="356" viewBox="0 0 443 356">
    <defs>
      <linearGradient id="villa" x1="0" y1="0" x2="0" y2="1">
        <stop offset="0" stop-color="#7b8ea3"/><stop offset=".55" stop-color="#9a8a74"/><stop offset="1" stop-color="#4d6a78"/>
      </linearGradient>
      <linearGradient id="stand" x1="0" y1="0" x2="0" y2="1">
        <stop offset="0" stop-color="#e4e4e4"/><stop offset="1" stop-color="#a9a9a9"/>
      </linearGradient>
    </defs>
    <rect x="0" y="0" width="443" height="275" rx="8" fill="#111"/>
    <rect x="0" y="250" width="443" height="30" rx="4" fill="#d9d9d9"/>
    <rect x="17" y="20" width="409" height="225" fill="url(#villa)" role="img" aria-label="Video still of a luxury villa with a pool"/>
    <circle cx="221" cy="133" r="26" fill="rgba(255,255,255,.85)"/>
    <path d="M212 118l24 15-24 15z" fill="#444"/>
    <path d="M180 280h83l10 62h-103z" fill="url(#stand)"/>
    <ellipse cx="221" cy="346" rx="72" ry="8" fill="#c9c9c9"/>
  </svg>
</section>

<!-- services -->
<section class="services">
  <h2 class="sec-title" style="top:46px">Our Services</h2>
  <svg class="sec-rule" style="top:103px" viewBox="0 0 240 14"><path d="M0 12H108L120 2 132 12H240" stroke="#b8b8b8" fill="none"/><path d="M113 12l7-6 7 6" stroke="#b8b8b8" fill="none"/></svg>

  <div class="cat-line" style="left:100px;top:162px;width:1000px"></div>
  <div class="cat" style="left:455px;top:144px;width:288px">Administration Services</div>

  <div class="card active" style="left:100px;top:212px">
    <div class="overlay" role="img" aria-label="Close-up of a hand stacking coins, darkened for hover text">
      <h3>Treasury</h3>
      <p>Duis autem vel eum iriure dolor in hendrerikmo ink vulputate velit esse molestie consequat, velmol illu</p>
      <svg class="plus" width="44" height="44" viewBox="0 0 44 44"><circle cx="22" cy="22" r="20" fill="none" stroke="#fff" stroke-width="1.5"/><path d="M22 12v20M12 22h20" stroke="#fff" stroke-width="1.5"/></svg>
    </div>
  </div>
  <div class="card" style="left:441px;top:212px">
    <div class="photo" role="img" aria-label="Hands working on financial charts with a calculator" style="background:linear-gradient(135deg,#dfe6f0,#9fb3cf 60%,#e8eaee)"></div>
    <svg class="badge" width="60" height="44" viewBox="0 0 60 44"><path d="M0 44V16L30 0 60 16v28z" fill="#fff"/><rect x="22" y="16" width="16" height="20" rx="2" fill="#222"/><rect x="25" y="19" width="10" height="4" fill="#fff"/></svg>
    <div class="label">Accounting</div>
  </div>
  <div class="card" style="left:784px;top:212px">
    <div class="photo" role="img" aria-label="Hand placing a coin on stacks of gold coins" style="background:linear-gradient(135deg,#f2efe9,#d9cdb5 55%,#b89656)"></div>
    <svg class="badge" width="60" height="44" viewBox="0 0 60 44"><path d="M0 44V16L30 0 60 16v28z" fill="#fff"/><ellipse cx="30" cy="26" rx="11" ry="8" fill="#222"/></svg>
    <div class="label">Savings</div>
  </div>

  <div class="cat-line" style="left:100px;top:496px;width:1000px"></div>
  <div class="cat" style="left:499px;top:478px;width:244px">Consulting Services</div>

  <div class="card" style="left:100px;top:546px">
    <div class="photo" role="img" aria-label="Wooden judge's gavel and brass scales" style="background:linear-gradient(135deg,#3b2414,#8a5526 55%,#2a1a10)"></div>
    <svg class="badge" width="60" height="44" viewBox="0 0 60 44"><path d="M0 44V16L30 0 60 16v28z" fill="#fff"/><path d="M22 36l10-10M26 18l10 10M30 14l10 10" stroke="#222" stroke-width="3"/></svg>
    <div class="label">Legal</div>
  </div>
  <div class="card" style="left:441px;top:546px">
    <div class="photo" role="img" aria-label="Interlocking metal gears in blue light" style="background:linear-gradient(135deg,#1e2f52,#5a6f94 50%,#1a2440)"></div>
    <svg class="badge" width="60" height="44" viewBox="0 0 60 44"><path d="M0 44V16L30 0 60 16v28z" fill="#fff"/><path d="M22 18l16 18M38 18L22 36" stroke="#222" stroke-width="3"/></svg>
    <div class="label">Technical</div>
  </div>
  <div class="card" style="left:784px;top:546px">
    <div class="photo" role="img" aria-label="People signing paperwork at a desk" style="background:linear-gradient(135deg,#eef1f6,#c6cfdc 60%,#8b98ab)"></div>
    <svg class="badge" width="60" height="44" viewBox="0 0 60 44"><path d="M0 44V16L30 0 60 16v28z" fill="#fff"/><rect x="25" y="16" width="10" height="12" fill="#222"/><rect x="20" y="28" width="20" height="6" fill="#222"/></svg>
    <div class="label">Regulatory</div>
  </div>

  <div class="cat-line" style="left:100px;top:833px;width:1000px"></div>
  <div class="cat" style="left:499px;top:814px;width:244px">Mediation Services</div>

  <div class="card" style="left:100px;top:887px">
    <div class="photo" role="img" aria-label="Family house with tools in the foreground" style="background:linear-gradient(180deg,#9ebad6,#c9c2b0 55%,#6e8d3e)"></div>
    <svg class="badge" width="60" height="44" viewBox="0 0 60 44"><path d="M0 44V16L30 0 60 16v28z" fill="#fff"/><circle cx="30" cy="27" r="8" fill="none" stroke="#222" stroke-width="4"/></svg>
    <div class="label">Repairs</div>
  </div>
  <div class="card" style="left:441px;top:887px">
    <div class="photo" role="img" aria-label="Business team gathered around a laptop in a meeting" style="background:linear-gradient(135deg,#f4f4f4,#b9b9b9 55%,#2e2e2e)"></div>
    <svg class="badge" width="60" height="44" viewBox="0 0 60 44"><path d="M0 44V16L30 0 60 16v28z" fill="#fff"/><circle cx="22" cy="22" r="3" fill="#222"/><circle cx="30" cy="22" r="3" fill="#222"/><circle cx="38" cy="22" r="3" fill="#222"/><rect x="18" y="28" width="24" height="6" fill="#222"/></svg>
    <div class="label">Meetings</div>
  </div>
  <div class="card" style="left:784px;top:887px">
    <div class="photo" role="img" aria-label="Hooded figure in black and white, hands bound" style="background:linear-gradient(135deg,#d8d8d8,#777 50%,#1e1e1e)"></div>
    <svg class="badge" width="60" height="44" viewBox="0 0 60 44"><path d="M0 44V16L30 0 60 16v28z" fill="#fff"/><circle cx="24" cy="27" r="5" fill="none" stroke="#222" stroke-width="3"/><circle cx="36" cy="27" r="5" fill="none" stroke="#222" stroke-width="3"/></svg>
    <div class="label">Delinquency</div>
  </div>
</section>

<!-- blog -->
<section class="blog">
  <h2 class="sec-title" style="top:50px">Latest Blog</h2>
  <svg class="sec-rule" style="top:107px" viewBox="0 0 240 14"><path d="M0 12H108L120 2 132 12H240" stroke="#b8b8b8" fill="none"/><path d="M113 12l7-6 7 6" stroke="#b8b8b8" fill="none"/></svg>

  <article class="post" style="left:100px">
    <div class="photo" role="img" aria-label="Madrid's business towers at dusk" style="background:linear-gradient(180deg,#6f7f9a,#b8a2a0 55%,#4a4846)"></div>
    <h3>Contrary To Popular Belief</h3>
    <div class="meta"><span>By Lucas Merino</span><span>December 06, 2016</span></div>
    <p>The standard chunk of lorem ipsum used since the reproduced below for those interested.</p>
    <div class="more">MORE <svg width="18" height="10" viewBox="0 0 18 10"><path d="M0 5h16M12 1l4 4-4 4" stroke="#fff" stroke-width="1.5" fill="none"/></svg></div>
  </article>
  <article class="post" style="left:441px">
    <div class="photo" role="img" aria-label="Glass skyscraper against a blue sky" style="background:linear-gradient(135deg,#d6e4f2,#6d8fb6 55%,#2b4a73)"></div>
    <h3>Contrary To Popular Belief</h3>
    <div class="meta"><span>By Lucas Merino</span><span>December 06, 2016</span></div>
    <p>The standard chunk of lorem ipsum used since the reproduced below for those interested.</p>
    <div class="more">MORE <svg width="18" height="10" viewBox="0 0 18 10"><path d="M0 5h16M12 1l4 4-4 4" stroke="#fff" stroke-width="1.5" fill="none"/></svg></div>
  </article>
  <article class="post" style="left:784px">
    <div class="photo" role="img" aria-label="Manhattan skyline under a clear sky" style="background:linear-gradient(180deg,#a9c3df,#8794a6 60%,#4d5563)"></div>
    <h3>Contrary To Popular Belief</h3>
    <div class="meta"><span>By Lucas Merino</span><span>December 06, 2016</span></div>
    <p>The standard chunk of lorem ipsum used since the reproduced below for those interested.</p>
    <div class="more">MORE <svg width="18" height="10" viewBox="0 0 18 10"><path d="M0 5h16M12 1l4 4-4 4" stroke="#fff" stroke-width="1.5" fill="none"/></svg></div>
  </article>
</section>
<svg class="carousel-arrow" style="left:48px" width="22" height="44" viewBox="0 0 22 44"><path d="M20 2L2 22l18 20" stroke="#aaa" stroke-width="2" fill="none"/></svg>
<svg class="carousel-arrow" style="left:1130px" width="22" height="44" viewBox="0 0 22 44"><path d="M2 2l18 20L2 42" stroke="#aaa" stroke-width="2" fill="none"/></svg>

<!-- footer -->
<footer class="footer">
  <h4 style="left:105px">Quick Links</h4>
  <ul class="quick-links">
    <li>Home</li><li>About Us</li><li>Services</li><li>Blog</li><li>Contact Us</li>
  </ul>

  <h4 style="left:332px">Quick Inquiry</h4>
  <div class="inq" style="top:98px">Name</div>
  <div class="inq" style="top:134px">Email</div>
  <div class="inq" style="top:170px;height:32px">Message</div>
  <div class="inq-submit">Submit</div>

  <h4 style="left:643px">Contact Details</h4>
  <div class="detail" style="top:100px">
    <svg width="11" height="15" viewBox="0 0 11 15"><path d="M5.5 0A5.5 5.5 0 0 0 0 5.5C0 10 5.5 15 5.5 15S11 10 11 5.5A5.5 5.5 0 0 0 5.5 0z" fill="#d4730f"/><circle cx="5.5" cy="5.5" r="2" fill="#676767"/></svg>
    <div>Portalia 720<br>123 mim ad minim veniam,<br>quis nostrud exerci</div>
  </div>
  <div class="detail" style="top:170px">
    <svg width="13" height="13" viewBox="0 0 14 14"><path d="M3 1l2.5 3-1.4 1.6a8 8 0 0 0 4.3 4.3L10 8.5 13 11l-1.5 2C6 13 1 8 1 2.5z" fill="#d4730f"/></svg>123 555 0190
  </div>
  <div class="detail" style="top:202px">
    <svg width="13" height="13" viewBox="0 0 14 14"><path d="M3 1l2.5 3-1.4 1.6a8 8 0 0 0 4.3 4.3L10 8.5 13 11l-1.5 2C6 13 1 8 1 2.5z" fill="#d4730f"/></svg>123 555 0190
  </div>
  <div class="detail" style="top:234px">
    <svg width="14" height="11" viewBox="0 0 16 12"><rect width="16" height="12" fill="#d4730f"/><path d="M0 0l8 6 8-6" stroke="#676767" stroke-width="1.5" fill="none"/></svg>inquiry@portalia720.example
  </div>
</footer>
<svg class="map" width="348" height="336" viewBox="0 0 348 336" role="img" aria-label="Street map showing the office location">
  <defs>
    <linearGradient id="mapTone" x1="0" y1="0" x2="1" y2="1">
      <stop offset="0" stop-color="#eef1e8"/><stop offset=".6" stop-color="#e2e6dc"/><stop offset="1" stop-color="#d8dfe6"/>
    </linearGradient>
  </defs>
  <path d="M45 0H348V336H0z" fill="url(#mapTone)"/>
  <path d="M190 130c-9 0-15 7-15 15 0 12 15 27 15 27s15-15 15-27c0-8-6-15-15-15z" fill="#d9382b"/>
  <circle cx="190" cy="145" r="5" fill="#8c1e16"/>
</svg>
<div class="bottom-bar">
  <div class="copy">Copyright © 2017 Portalia 720. All Rights Reserved.</div>
  <div class="round" style="left:694px"></div>
  <div class="round" style="left:727px"></div>
  <div class="round" style="left:760px"></div>
  <div class="round" style="left:793px"></div>
</div>

</body>
</html>
```